Diagramm/Grafik zur Darstellung einer Formel
Zielgruppe
Das Unternehmen ist in der Unternehmensberatung tätig und beschäftigt sich mit der Analyse von IT-In- und Outsourcing.
Zielgruppe: Entscheider / Höheres Management / Round Table
Aufgabenstellung
Es wurde für die Bewertung des bestehenden Outsourcing eine Formel entwickelt, welche es ermöglicht einerseits die Stärken
und Schwächen und andererseits die Entwicklung und Vorteilhaftigkeit der Kosten für die nächsten Jahre zu prognostizieren.
Der Name der Formel ist "MIRAX-P Methode" (Strategie, Technologie, Organisation, Qualität und Kosten)
Die Formel ist aufgebaut aus 5 Sektoren, unter welchem jeweils 3-8 Faktoren untergeordnet sind. (siehe IMG_1159)
Die Zuordnung der Faktoren zu Sektoren (siehe SektorenFaktoren.pdf) ist variabel, aus welchem Grund unter jedem Sektor 3-8 Faktoren unterordnenbar sein sollten.
Grundsätzlich findet die Auswertung aus dem Vergleich von Kosten + Risiken - Chancen jeweils von Outsourcing und Insourcing statt. (siehe IMG_1190)
Ziel ist es, eine Darstellung der Sektoren und Faktoren sowie der Formel zu finden, welche:
a) die Abhängigkeit von den Faktoren zu den Sektoren darstellt
b) die Formel darstellt
c) sich als Ganzes oder in Teilen für diverse Unterlagen verwenden lässt (bspw. .pptx, .pdf, etc.)
--> es ist geplant diese Darstellung bspw. als Ganzes oder in Teilen in eine PowerPoint-Präsentation zu integrieren
Diese Aufgabenstellung ist ein erster Versuch mittels der Plattform pixelhafen.de Aufträge zu vergeben.
Bei Erfolg sind Anschlussaufträge geplant.
WICHTIG: Alle Anhänge diesen lediglich zur Darstellung der Zusammenhänge, sollen aber keinerlei design vorgeben!

```html
<!DOCTYPE html>
<html lang="de">
<head>
<meta charset="utf-8">
<title>MIRAX-P</title>
<link href="https://fonts.googleapis.com/css2?family=Barlow:wght@400;500;600;700&display=swap" rel="stylesheet">
<style>
:root{
  --band:#587a9c;
  --band-light:#8fa7bd;
  --orange:#e05a1a;
  --ink:#555a5f;
  --muted:#6f7880;
  --soft:#f0f0f0;
  --white:#ffffff;
}
*{margin:0;padding:0;box-sizing:border-box}
html,body{width:1200px;height:900px;overflow:hidden;background:var(--white)}
body{font-family:"Barlow",Arial,sans-serif;color:var(--ink)}
.canvas{position:relative;width:1200px;height:900px;overflow:hidden;background:var(--white)}
.header{position:absolute;left:0;top:0;width:1200px;height:62px;background:var(--band);border-bottom:6px solid var(--band-light);
  display:flex;align-items:center;justify-content:center;color:var(--white);font-weight:600;font-size:42px;letter-spacing:8px}
.shapes{position:absolute;left:0;top:0;width:1200px;height:492px}
.side-title{position:absolute;top:136px;width:400px;text-align:center;font-weight:700;font-size:34px;letter-spacing:5px;color:var(--orange)}
.formula{position:absolute;top:257px;font-size:29px;font-weight:500;color:var(--ink);white-space:nowrap}
.formula .accent{color:var(--orange)}
.num{position:absolute;width:22px;height:22px;border-radius:50%;background:var(--band-light);color:var(--white);
  font-size:13px;font-weight:600;display:flex;align-items:center;justify-content:center;transform:translate(-50%,-50%)}
.compare{position:absolute;left:450px;top:420px;width:300px;text-align:center;font-size:16px;color:var(--band-light)}
.compare .accent{color:var(--orange)}
.factors{position:absolute;left:0;top:492px;width:1200px;height:396px;background:var(--soft);border-top:6px solid var(--band)}
.footer-band{position:absolute;left:0;bottom:0;width:1200px;height:12px;background:var(--band-light)}
.sector{position:absolute}
.sector-head{display:flex;align-items:center;gap:4px;font-size:12px;font-weight:600;color:var(--ink);letter-spacing:.3px;height:20px}
.sector-head .dot{width:18px;height:18px;border-radius:50%;background:var(--band-light);color:var(--white);font-size:12px;display:flex;align-items:center;justify-content:center}
.sector ol{list-style:none;margin-left:17px;font-size:11px;line-height:16px;color:var(--muted)}
.method-mark{position:absolute;right:36px;bottom:18px;font-size:31px;font-weight:700;color:var(--orange);letter-spacing:1px}
</style>
</head>
<body>
<div class="canvas">
  <header class="header">MIRAX-P</header>

  <svg class="shapes" viewBox="0 0 1200 492" aria-hidden="true">
    <g fill="none" stroke="var(--orange)" stroke-width="5" stroke-linecap="round">
      <path d="M63,248 Q63,215 100,215 L225,215 Q255,215 255,190 Q255,215 285,215 L410,215 Q447,215 447,248"/>
      <path d="M755,248 Q755,215 792,215 L915,215 Q945,215 945,190 Q945,215 975,215 L1098,215 Q1135,215 1135,248"/>
    </g>
    <g fill="none" stroke="var(--band-light)" stroke-width="3" stroke-linecap="round">
      <path d="M150,302 Q150,327 175,327 L268,327 Q294,327 294,350 Q294,327 320,327 L413,327 Q438,327 438,302"/>
      <path d="M837,306 Q837,331 862,331 L950,331 Q975,331 975,354 Q975,331 1000,331 L1088,331 Q1113,331 1113,306"/>
    </g>
    <g fill="none" stroke="var(--band-light)" stroke-width="2">
      <line x1="188" y1="342" x2="188" y2="396" stroke-dasharray="4 4"/>
      <line x1="387" y1="342" x2="387" y2="396" stroke-dasharray="4 4"/>
      <line x1="870" y1="346" x2="870" y2="402" stroke-dasharray="4 4"/>
      <line x1="1068" y1="346" x2="1068" y2="402" stroke-dasharray="4 4"/>
      <path d="M182,392 L188,400 L194,392"/>
      <path d="M381,392 L387,400 L393,392"/>
      <path d="M864,398 L870,406 L876,398"/>
      <path d="M1062,398 L1068,406 L1074,398"/>
      <rect x="573" y="230" width="60" height="90" stroke-dasharray="3 3"/>
      <path d="M590,244 L616,254 L590,264" stroke-width="2.5"/>
      <line x1="590" y1="270" x2="616" y2="270" stroke-width="2.5"/>
      <line x1="590" y1="280" x2="616" y2="280" stroke-width="2.5"/>
      <path d="M616,286 L590,296 L616,306" stroke-width="2.5"/>
      <line x1="603" y1="327" x2="603" y2="400" stroke-width="2.5"/>
      <path d="M583,378 L603,402 L623,378" stroke-width="2.5"/>
    </g>
  </svg>

  <div class="side-title" style="left:55px">OUTSOURCING</div>
  <div class="formula" style="left:60px">OS + <span class="accent">(</span>Chancen - Risiken<span class="accent">)*</span></div>
  <span class="num" style="left:130px;top:423px">1</span>
  <span class="num" style="left:166px;top:423px">2</span>
  <span class="num" style="left:202px;top:423px">3</span>
  <span class="num" style="left:240px;top:423px">4</span>
  <span class="num" style="left:385px;top:423px">5</span>

  <div class="compare">Vergleich der Nutzen v. <span class="accent">Is / Os</span></div>

  <div class="side-title" style="left:745px">INSOURCING</div>
  <div class="formula" style="left:755px">IS + <span class="accent">(</span>Chancen - Risiken<span class="accent">)*</span></div>
  <span class="num" style="left:811px;top:429px">1</span>
  <span class="num" style="left:849px;top:429px">2</span>
  <span class="num" style="left:888px;top:429px">3</span>
  <span class="num" style="left:925px;top:429px">4</span>
  <span class="num" style="left:1068px;top:429px">5</span>

  <section class="factors">
    <div class="sector" style="left:51px;top:22px"><div class="sector-head"><span class="dot">1</span>STRATEGIE</div><ol><li>1.</li><li>2.</li><li>3.</li><li>4.</li><li>5.</li><li>6.</li><li>7.</li><li>8.</li></ol></div>
    <div class="sector" style="left:179px;top:22px"><div class="sector-head"><span class="dot">2</span>TECHNOLOGIE</div><ol><li>1.</li><li>2.</li><li>3.</li><li>4.</li><li>5.</li><li>6.</li><li>7.</li><li>8.</li></ol></div>
    <div class="sector" style="left:374px;top:22px"><div class="sector-head"><span class="dot">5</span>KOSTEN</div><ol><li>1.</li><li>2.</li><li>3.</li><li>4.</li><li>5.</li><li>6.</li><li>7.</li><li>8.</li></ol></div>
    <div class="sector" style="left:51px;top:187px"><div class="sector-head"><span class="dot">3</span>ORGANISATION</div><ol><li>1.</li><li>2.</li><li>3.</li><li>4.</li><li>5.</li><li>6.</li><li>7.</li><li>8.</li></ol></div>
    <div class="sector" style="left:179px;top:187px"><div class="sector-head"><span class="dot">4</span>QUALITÄT</div><ol><li>1.</li><li>2.</li><li>3.</li><li>4.</li><li>5.</li><li>6.</li><li>7.</li><li>8.</li></ol></div>

    <div class="sector" style="left:756px;top:22px"><div class="sector-head"><span class="dot">1</span>STRATEGIE</div><ol><li>1.</li><li>2.</li><li>3.</li><li>4.</li><li>5.</li><li>6.</li><li>7.</li><li>8.</li></ol></div>
    <div class="sector" style="left:888px;top:22px"><div class="sector-head"><span class="dot">2</span>TECHNOLOGIE</div><ol><li>1.</li><li>2.</li><li>3.</li><li>4.</li><li>5.</li><li>6.</li><li>7.</li><li>8.</li></ol></div>
    <div class="sector" style="left:1056px;top:22px"><div class="sector-head"><span class="dot">5</span>KOSTEN</div><ol><li>1.</li><li>2.</li><li>3.</li><li>4.</li><li>5.</li><li>6.</li><li>7.</li><li>8.</li></ol></div>
    <div class="sector" style="left:756px;top:187px"><div class="sector-head"><span class="dot">3</span>ORGANISATION</div><ol><li>1.</li><li>2.</li><li>3.</li><li>4.</li><li>5.</li><li>6.</li><li>7.</li><li>8.</li></ol></div>
    <div class="sector" style="left:888px;top:187px"><div class="sector-head"><span class="dot">4</span>QUALITÄT</div><ol><li>1.</li><li>2.</li><li>3.</li><li>4.</li><li>5.</li><li>6.</li><li>7.</li><li>8.</li></ol></div>

    <div class="method-mark">*MIRAX-P</div>
  </section>
  <div class="footer-band"></div>
</div>
</body>
</html>
```